Birch Harbor - Countertop fabricator
Need stationary, business card and T-shirt design
Birch Harbor - Countertop fabricator -
Creative Brief
Simple
Kevin Rasble
14 Larkwood Lane Syracuse, NY13099
info@birchharborny.example
www.birchharborny.example
Back of card to list materials; Granite Quatz Marble Soapstone Solid Surface

```html
<!DOCTYPE html>
<html lang="en">
<head>
<meta charset="utf-8">
<title>Birch Harbor Stationery</title>
<link rel="stylesheet" href="https://fonts.googleapis.com/css2?family=Tinos:wght@400;700&display=swap">
<style>
  :root {
    --bronze: #8a6733;
    --bronze-dark: #6f5128;
    --ink: #3b3b3b;
    --ink-soft: #666;
    --paper: #ffffff;
    --frame: #d9d9d9;
    --rule: #c9a66b;
  }
  * { margin: 0; padding: 0; box-sizing: border-box; }
  html, body { width: 1200px; height: 919px; overflow: hidden; background: var(--paper); }
  body { font-family: "Tinos", "Times New Roman", serif; color: var(--ink); }

  .canvas {
    position: relative; width: 1200px; height: 919px;
    border: 2px solid var(--frame); background: var(--paper);
  }

  .sheet { position: absolute; background: var(--paper); box-shadow: 3px 4px 7px rgba(0,0,0,.28); }

  .brand { display: flex; flex-direction: column; align-items: center; gap: 6px; }
  .brand-square { background: var(--bronze); }
  .brand-name { font-weight: 400; color: var(--ink); white-space: nowrap; letter-spacing: -0.3px; }

  /* Letterhead */
  .letterhead { left: 408px; top: 48px; width: 450px; height: 797px; }
  .letterhead .brand { position: absolute; left: 0; right: 0; top: 46px; }
  .letterhead .brand-square { width: 40px; height: 40px; margin-left: 40px; }
  .letterhead .brand-name { font-size: 26px; }
  .letterhead-rule { position: absolute; left: 40px; right: 40px; top: 747px; height: 1px; background: var(--rule); }
  .letterhead-footer {
    position: absolute; left: 0; right: 0; top: 759px; text-align: center;
    font-size: 8.5px; color: var(--ink-soft); white-space: nowrap;
  }

  /* Envelope */
  .envelope { left: 70px; top: 330px; width: 725px; height: 410px; background: none; box-shadow: none; }
  .envelope svg { position: absolute; left: 0; top: 0; filter: drop-shadow(3px 4px 4px rgba(0,0,0,.28)); }
  .envelope .brand { position: absolute; left: 14px; top: 133px; align-items: flex-start; }
  .envelope .brand-square { width: 42px; height: 42px; margin-left: 12px; }
  .envelope .brand-name { font-size: 24px; }
  .envelope-address { position: absolute; left: 18px; top: 230px; font-size: 9px; color: var(--ink-soft); }

  /* Business cards */
  .card { left: 875px; width: 253px; height: 143px; }
  .card-front { top: 258px; }
  .card-front .brand-square { position: absolute; left: 116px; top: 10px; width: 24px; height: 24px; }
  .card-holder { position: absolute; left: 0; right: 0; top: 60px; text-align: center; font-size: 12px; }
  .card-rule { position: absolute; left: 14px; right: 14px; top: 91px; height: 1px; background: var(--rule); }
  .card-contact {
    position: absolute; left: 0; right: 0; top: 96px; text-align: center;
    font-size: 5.5px; line-height: 7.5px; color: var(--ink-soft); white-space: nowrap;
  }

  .card-back { top: 430px; height: 145px; }
  .card-back .brand { position: absolute; left: 0; right: 0; top: 28px; }
  .card-back .brand-square { width: 38px; height: 38px; margin-left: 40px; }
  .card-back .brand-name { font-size: 20px; margin-left: 40px; }
  .materials {
    position: absolute; left: 0; right: 0; top: 117px; display: flex; justify-content: center; gap: 7px;
    font-size: 6.5px; font-weight: 700; color: var(--ink); list-style: none;
  }
  .materials li::before { content: ""; display: inline-block; width: 4px; height: 4px; background: var(--ink); margin-right: 3px; vertical-align: 1px; }
</style>
</head>
<body>
<main class="canvas">

  <section class="sheet envelope" aria-label="Envelope">
    <svg width="725" height="410" viewBox="0 0 725 410">
      <rect x="0" y="0" width="725" height="410" rx="4" fill="var(--paper)"/>
      <path d="M0 132 L0 12 Q0 0 12 0 L713 0 Q725 0 725 12 L725 132 L712 132 Q705 132 700 128 L690 124 L35 124 L25 128 Q20 132 13 132 Z" fill="var(--bronze)"/>
    </svg>
    <div class="brand">
      <div class="brand-square"></div>
      <div class="brand-name">Birch Harbor</div>
    </div>
    <p class="envelope-address">14 Larkwood Lane, Syracuse, NY13099</p>
  </section>

  <section class="sheet letterhead" aria-label="Letterhead">
    <div class="brand">
      <div class="brand-square"></div>
      <div class="brand-name">Birch Harbor</div>
    </div>
    <div class="letterhead-rule"></div>
    <p class="letterhead-footer">14 Larkwood Lane, Syracuse, NY13099 &nbsp;|&nbsp; Phone: 315-555-0142 &nbsp;|&nbsp; Fax: 607-555-0187 &nbsp;|&nbsp; www.birchharborny.example</p>
  </section>

  <section class="sheet card card-front" aria-label="Business card front">
    <div class="brand-square"></div>
    <p class="card-holder">Kevin Rasble</p>
    <div class="card-rule"></div>
    <p class="card-contact">14 Larkwood Lane Syracuse, NY13099<br>Phone: 315-555-0142 &nbsp;| Cell: 315-555-0163 &nbsp;| Fax: 607-555-0187<br>Email: info@birchharborny.example &nbsp;| www.birchharborny.example</p>
  </section>

  <section class="sheet card card-back" aria-label="Business card back">
    <div class="brand">
      <div class="brand-square"></div>
      <div class="brand-name">Birch Harbor</div>
    </div>
    <ul class="materials">
      <li>Granite</li><li>Quartz</li><li>Marble</li><li>Soapstone</li><li>Solid Surface</li>
    </ul>
  </section>

</main>
</body>
</html>
```